Brochure Design Project (Design Studio)

Items required:
1-Brochure. We suggest 15Cm X 15 Cm after cutting.
2-Business Card.
3-Head letter.
4-Folder ( folder should carry the Brochure in pocket and the business card in a pocket on the opposite side of the folder.
5-Envelope to carry everything.
This brochure is expected to draw attention of high level management in companies to the quality and creativity of the design work and encourage them to do business with us. note that brochure will be printed in high quality printing and paper.
The game plan is as follows:
Over all description, the theme of the brochure is drawn from the website theme (website will be uploaded shortly, pictures of the website are attached, logo appears in the top left corner). Please avoid direct copying from the website unless it is a creative copying, just draw the theme from there. however, we need it to be elegant, stylish and class in colors and style. This is a MUST.
Furthermore, the main items of the Brochure:
1-The Studio is not just a studio: we will take about how Branding. A file is attached of the content. (slight changes/modification can apply during the designing process)
2-The Process: this one has to be a visual illustration of the process, it has to be very creative, could be elegant arrows and comics, could be elegant drawing, could be an elegant icons. The drawing should be separate from the steps, we need to the drawing and we need to have the steps listed and commentary, or if want to integrate both in one in an artistic way. Just don’t lose track of the theme and elegance. (steps and commentary are attached, slight changes/modification can apply at anytime.
3-Our Team: another drawing of your suggestion to illustrate the team members, we need to include the names and designation as well leave a place for some of them to say what they need to say about their style of designing. I leave it for your imagination to put this all together in a nice attractive visual illustration.
4-Works: this section will generally show the works of our designers. It needs to be focused on the works themselves, client should be able to view the details of the works ( note that when it comes to brochures and websites, we don’t need to reach to the extent with which the client can read the text in those pictures of the website or brochure, but still can see the overall design clearly). Each design is to carry the name of the designer. Last thing, this section will classify works into categories, like, Brochures, Corporate identity, print design. We didn’t finalize those categories, we will provide them to you shortly, last thing to be said, we are planning to include around 25-30 designs of each sub-category, eg. Corporate identity will have 30 business card s designs and 30 stationary designs.
5-Contacts: the company contacts.
We the brochure after printing should be 15x15 Cm.
Creativity and art work is a major player in selection.
general managers, owners
Printing

```html
<!DOCTYPE html>
<html lang="en">
<head>
<meta charset="utf-8">
<title>Lumenvale Studio — Brochure Cover Spread</title>
<link rel="stylesheet" href="https://fonts.googleapis.com/css2?family=Open+Sans:wght@300;400&display=swap">
<style>
  :root {
    --bg-center: #50646c;
    --bg-mid: #33444c;
    --bg-edge: #1d2a31;
    --ink-white: #ffffff;
    --ink-soft: #dfe4e6;
    --ink-muted: #c9d0d3;
  }
  html, body {
    margin: 0;
    padding: 0;
    width: 1200px;
    height: 849px;
    overflow: hidden;
  }
  .spread {
    position: relative;
    width: 1200px;
    height: 849px;
    background: radial-gradient(ellipse 640px 520px at 600px 420px,
      var(--bg-center) 0%, var(--bg-mid) 45%, var(--bg-edge) 100%);
    font-family: "Open Sans", "Helvetica Neue", Arial, sans-serif;
    color: var(--ink-white);
    overflow: hidden;
  }
  .brand-mark {
    position: absolute;
    right: 798px;
    top: 362px;
    margin: 0;
    font-weight: 300;
    font-size: 46px;
    line-height: 1;
    letter-spacing: 0.5px;
    white-space: nowrap;
    color: var(--ink-white);
  }
  .web-address {
    position: absolute;
    left: 416px;
    top: 367px;
    font-size: 11px;
    font-weight: 400;
    white-space: nowrap;
    color: var(--ink-soft);
  }
  .brand-lockup {
    position: absolute;
    left: 730px;
    top: 354px;
    margin: 0;
    display: flex;
    align-items: baseline;
    gap: 12px;
    white-space: nowrap;
  }
  .brand-name {
    font-weight: 300;
    font-size: 24px;
    line-height: 1;
    letter-spacing: 0.5px;
    color: var(--ink-white);
  }
  .brand-descriptor {
    font-weight: 400;
    font-size: 11px;
    letter-spacing: 1.6px;
    color: var(--ink-soft);
  }
  .tagline {
    position: absolute;
    left: 786px;
    top: 597px;
    margin: 0;
    font-weight: 300;
    font-size: 16px;
    letter-spacing: 0.8px;
    white-space: nowrap;
    color: var(--ink-soft);
  }
  .contact-block {
    position: absolute;
    left: 198px;
    top: 762px;
    width: 200px;
    margin: 0;
    font-style: normal;
    font-size: 10px;
    line-height: 13px;
    text-align: center;
    color: var(--ink-muted);
  }
</style>
</head>
<body>
  <main class="spread">
    <section class="back-cover">
      <p class="brand-mark">Lumenvale</p>
      <span class="web-address">www.lumenvalestudio.com</span>
      <address class="contact-block">
        Tel: 00 971 2 555 0142<br>
        Fax: 00 971 2 555 0143<br>
        hello@lumenvalestudio.com<br>
        P.O. Box 40210, Abu Dhabi, UAE
      </address>
    </section>
    <section class="front-cover">
      <h1 class="brand-lockup">
        <span class="brand-name">Lumenvale Studio</span>
        <span class="brand-descriptor">KREATIVE DESIGNS</span>
      </h1>
      <p class="tagline">PEROSNIFY YOUR BUSINESS</p>
    </section>
  </main>
</body>
</html>
```